Design interface for an invoicing software

We are developing a new invoicing software that is a very boring topic. Users can use the software to write invoices and manage their income. Therefore we want to inspire the users with a great desgin. By this we mean, for example, the use of photos in the background (streets in New York, landscapes), or "crazy" looking headlines or something else. Target group are young start-ups, freelancers, hairdressers and taxi drivers at the age of 18-40 years. It would also be worth considering to adapt the look to the user's industry. However, the menu items themselves and the approximate position of the information are given. See file "startpoint" What kind of ideas do you have?

Europe

Small Business

Designer to choose colors to be used in the design.

• the menu items themselves and the approximate position of the information are given. The navigation menu itself can be different.
• boring look and feel

```html
<!DOCTYPE html>
<html lang="en">
<head>
<meta charset="utf-8">
<title>Invoicing Dashboard</title>
<link rel="stylesheet" href="https://fonts.googleapis.com/css2?family=Montserrat:wght@600;700&family=Lato:wght@400;700&display=swap">
<style>
  :root {
    --ink: #ffffff;
    --ink-muted: rgba(255,255,255,0.55);
    --ink-faint: rgba(255,255,255,0.35);
    --rule-faint: rgba(255,255,255,0.25);
    --overdue: #ff1f6b;
    --paid: #2ef0a0;
    --dot-today: #19d3f5;
    --dot-tomorrow: #ff9a1a;
    --legend-expenses: #23f08a;
    --legend-income: #ff1ee0;
    --bg-top: #3a3b3e;
    --bg-mid: #2a2b2d;
    --bg-bottom: #1c1d1e;
  }
  * { margin: 0; padding: 0; box-sizing: border-box; }
  html, body { width: 1200px; height: 675px; overflow: hidden; }
  body { font-family: "Lato", Arial, sans-serif; color: var(--ink); }
  .dashboard { position: relative; width: 1200px; height: 675px; overflow: hidden; }
  .backdrop {
    position: absolute; inset: 0;
    background:
      radial-gradient(ellipse at 50% 20%, rgba(90,92,96,0.55), transparent 55%),
      linear-gradient(180deg, var(--bg-top) 0%, var(--bg-mid) 55%, var(--bg-bottom) 100%);
  }
  .abs { position: absolute; }
  .menu-toggle { left: 61px; top: 64px; width: 25px; height: 18px; }
  .window-controls { left: 1070px; top: 22px; width: 110px; height: 26px; }
  .section-title {
    font-family: "Montserrat", Arial, sans-serif; font-weight: 700;
    font-size: 42px; line-height: 1; letter-spacing: 0.2px;
  }
  .invoices-title { left: 135px; top: 157px; }
  .todo-title { left: 787px; top: 157px; }
  .stats-title { left: 135px; top: 534px; }
  .add-task { left: 957px; top: 164px; width: 28px; height: 28px; }

  .rail { width: 2px; }
  .rail.strong { background: var(--ink); }
  .rail.soft { background: var(--rule-faint); width: 1px; }

  .invoice { position: absolute; left: 175px; width: 526px; height: 44px; }
  .invoice .client { position: absolute; left: 0; top: 0; font-weight: 700; font-size: 16px; }
  .invoice .issued { position: absolute; left: 0; top: 24px; font-size: 13.5px; }
  .invoice .amount {
    position: absolute; right: 0; top: -3px; font-size: 21px; line-height: 1;
  }
  .invoice .amount sup { font-size: 11px; vertical-align: top; position: relative; top: -1px; margin-right: 1px; }
  .invoice .amount.overdue { color: var(--overdue); }
  .invoice .amount.paid { color: var(--paid); }
  .invoice .due { position: absolute; right: 0; top: 24px; font-weight: 700; font-size: 13.5px; }

  .day-label {
    font-family: "Montserrat", Arial, sans-serif; font-weight: 700;
    font-size: 11px; letter-spacing: 1px; color: var(--ink-muted); left: 834px;
  }
  .task { position: absolute; left: 834px; width: 340px; height: 20px; }
  .task .time { position: absolute; left: 0; top: 0; font-weight: 700; font-size: 14px; }
  .task .dot { position: absolute; left: 56px; top: 6px; width: 8px; height: 8px; border-radius: 50%; background: var(--dot-today); }
  .task .dot.tomorrow { background: var(--dot-tomorrow); }
  .task .label { position: absolute; left: 84px; top: 0; font-size: 14px; }
  .connector { left: 894px; width: 1px; height: 20px; background: var(--ink-muted); }

  .period-tabs { left: 135px; top: 595px; display: flex; gap: 0; }
  .period-tabs span {
    font-family: "Montserrat", Arial, sans-serif; font-weight: 700;
    font-size: 11px; letter-spacing: 1px; color: var(--ink-faint);
  }
  .period-tabs .active { color: var(--ink); width: 88px; }
  .period-tabs .month { width: 101px; }

  .legend { left: 501px; top: 552px; display: flex; align-items: center; font-family: "Montserrat", Arial, sans-serif; font-weight: 700; font-size: 14.5px; }
  .legend .swatch { width: 10px; height: 10px; margin-right: 7px; }
  .legend .expenses { background: var(--legend-expenses); }
  .legend .income { background: var(--legend-income); margin-left: 37px; }
</style>
</head>
<body>
<main class="dashboard">
  <div class="backdrop" role="img" aria-label="Darkened photo of a busy New York City avenue lined with tall buildings, trees and yellow taxis"></div>

  <svg class="abs menu-toggle" viewBox="0 0 25 18" aria-label="Menu">
    <rect x="0" y="0" width="25" height="2.4" fill="#fff"/>
    <rect x="0" y="7.8" width="25" height="2.4" fill="#fff"/>
    <rect x="0" y="15.6" width="25" height="2.4" fill="#fff"/>
  </svg>

  <svg class="abs window-controls" viewBox="0 0 110 26" aria-label="Window controls">
    <line x1="3" y1="19" x2="21" y2="19" stroke="#fff" stroke-width="2"/>
    <rect x="49" y="5" width="15" height="14" fill="none" stroke="#fff" stroke-width="2.4"/>
    <line x1="92" y1="4" x2="106" y2="18" stroke="#fff" stroke-width="2"/>
    <line x1="106" y1="4" x2="92" y2="18" stroke="#fff" stroke-width="2"/>
  </svg>

  <h1 class="abs section-title invoices-title">Invoices</h1>
  <div class="abs rail strong" style="left:135px; top:221px; height:199px;"></div>
  <div class="abs rail soft" style="left:136px; top:420px; height:63px;"></div>

  <div class="invoice" style="top:231px;">
    <span class="client">Mira Halden</span><span class="issued">17/29/2018</span>
    <span class="amount"><sup>$</sup>246</span><span class="due">Due on Sept 25, 2018</span>
  </div>
  <div class="invoice" style="top:302px;">
    <span class="client">Theo Brandt</span><span class="issued">17/29/2018</span>
    <span class="amount overdue"><sup>$</sup>127.80</span><span class="due">Due on Sept 25, 2018</span>
  </div>
  <div class="invoice" style="top:373px;">
    <span class="client">Owen Castell</span><span class="issued">17/29/2018</span>
    <span class="amount paid"><sup>$</sup>56.05</span><span class="due">Due on Sept 25, 2018</span>
  </div>
  <div class="invoice" style="top:445px;">
    <span class="client">Lena Marsh</span><span class="issued">17/29/2018</span>
    <span class="amount"><sup>$</sup>246</span><span class="due">Due on Sept 25, 2018</span>
  </div>

  <h2 class="abs section-title todo-title">To - do</h2>
  <svg class="abs add-task" viewBox="0 0 28 28" aria-label="Add task">
    <circle cx="14" cy="14" r="13" fill="none" stroke="#fff" stroke-width="1.4"/>
    <line x1="14" y1="8.5" x2="14" y2="19.5" stroke="#fff" stroke-width="1.4"/>
    <line x1="8.5" y1="14" x2="19.5" y2="14" stroke="#fff" stroke-width="1.4"/>
  </svg>
  <div class="abs rail strong" style="left:794px; top:221px; height:130px;"></div>
  <div class="abs rail soft" style="left:795px; top:351px; height:115px;"></div>

  <span class="abs day-label" style="top:226px;">TODAY</span>
  <div class="task" style="top:261px;"><span class="time">14:20</span><span class="dot"></span><span class="label">Yoga class with Rafi</span></div>
  <div class="abs connector" style="top:283px;"></div>
  <div class="task" style="top:305px;"><span class="time">16:40</span><span class="dot"></span><span class="label">Yoga class with Dario</span></div>
  <div class="abs connector" style="top:327px;"></div>
  <div class="task" style="top:350px;"><span class="time">16:40</span><span class="dot"></span><span class="label">Webinar with Elias.</span></div>

  <span class="abs day-label" style="top:420px;">TOMMOROW</span>
  <div class="task" style="top:448px;"><span class="time">16:40</span><span class="dot tomorrow"></span><span class="label">Appointment with Owen Castell</span></div>

  <h2 class="abs section-title stats-title">Statistics</h2>
  <div class="abs legend">
    <span class="swatch expenses"></span>Expenses
    <span class="swatch income"></span>Income
  </div>
  <nav class="abs period-tabs">
    <span class="active">YEAR</span><span class="month">MONTH</span><span>WEEK</span>
  </nav>
</main>
</body>
</html>
```